Awesome law firm seeks great artwork for sign to be installed at local roller skating rink!!

We're a dynamic, law firm that does its work with a difference - we actually care about our clients and our fees are usually lower than most other firms.

We are installing a sign that's 78cm (height) x 158cm (width) to be printed on 3mm Aluminum Composite Panel and installed at a local roller skating rink in Kalamunda, Perth, Western Australia.

Graphics need to be provided in vector .eps (Encapsulated Post Script), .ai (Adobe Illustrator) or PDF format.

We have uploaded a copy of our Logo, which should feature on the sign (we usually have it on the top right of our stationery, but are happy to see other suggestions), together with our practice areas - Family Law, Wills and Estates, Building and Construction, Corporate and Commercial, Local Government, General legal (personal or business).

We don't have a 'slogan' for our firm, but for the roller skating rink sign, we're thinking of something like 'We roll with you", or something similar. Surprise us :)

Sign should also indicate that our team are local to "the Hills", which is how this area (the Kalamunda and surrounding areas of Perth) is known.

Main colors of the sign can include blue, white, black and red (more blue, white and black preferred).

The final design should communicate trust and expertise in law, but have a fun edge (the sign's at a roller skating rink after all and will be seen on every lap as it's in the rink).

The sign must include our website address www.pelbarnlegal.com (note this is still under construction in case you google us :)), our phone number 0491 607 238 and our main email address, which is admin@pelbarnlegal.com

Beyond this, we're happy to see any cool ideas for the design of our sign.

Target Market(s)

Local families and business owners at local roller skating rink

Industry/Entity Type

Legal services

Font styles to use
Serif
Other font styles liked:
• Designer to choose

Colors
0054AA
0677BA
7BADD7
CADEEF
E8F1F8
EB3D1F
EC4F4E
F09395
F8D3D4
FCEDEE

Requirements
Must have
• Logo, contact details, design as per description and can have the words "Get your skates on!"
Nice to have
• Awesome, striking, appealing design - easy to read as you're zooming past on your skates!
Should not have
• Any offensive, explicit, corny or suggestive words and preferably avoid cliché rhyming catch phrases, albeit we do want something fun that has a skating vibe

```html
<!DOCTYPE html>
<html lang="en">
<head>
<meta charset="utf-8">
<title>Pelbarn Legal – Rink Sign</title>
<link href="https://fonts.googleapis.com/css2?family=Poppins:wght@400;500;600;700&family=Shrikhand&display=swap" rel="stylesheet">
<style>
  :root {
    --page-bg: #d9d9d9;
    --sign-dark: #1f2029;
    --brand-blue: #4274c5;
    --deep-blue: #0b3a98;
    --photo-blue-a: #2f63c8;
    --photo-blue-b: #123f96;
    --white: #ffffff;
    --grey-band: #4b4b4d;
    --outline-grey: #b3b3b3;
    --ink: #121212;
  }
  * { box-sizing: border-box; margin: 0; padding: 0; }
  html, body { width: 1200px; height: 1200px; overflow: hidden; }
  body { background: var(--page-bg); font-family: "Poppins", sans-serif; position: relative; }

  .sign {
    position: absolute; left: 50px; top: 328px;
    width: 1100px; height: 544px;
    background: var(--sign-dark); overflow: hidden;
  }
  .sign-art { position: absolute; inset: 0; }

  .headline { position: absolute; font-family: "Shrikhand", cursive; line-height: 1; white-space: nowrap; paint-order: stroke fill; }
  .headline-top {
    left: 40px; top: 20px; font-size: 112px; color: var(--brand-blue);
    -webkit-text-stroke: 12px var(--outline-grey);
  }
  .headline-bottom {
    left: 96px; top: 162px; font-size: 108px; color: var(--white);
    -webkit-text-stroke: 12px var(--ink);
  }

  .contact-band { position: absolute; left: 0; display: flex; align-items: center; color: var(--white); }
  .email-band {
    top: 321px; width: 324px; height: 91px; background: var(--grey-band);
    clip-path: polygon(0 0, 294px 0, 324px 100%, 0 100%);
    padding-left: 34px; gap: 10px;
  }
  .phone-band {
    top: 424px; width: 480px; height: 94px; background: var(--brand-blue);
    clip-path: polygon(0 0, 448px 0, 480px 100%, 0 100%);
    padding-left: 34px; gap: 14px;
  }
  .icon-disc {
    width: 58px; height: 58px; border-radius: 50%; background: var(--white);
    display: flex; align-items: center; justify-content: center; flex: none;
  }
  .email-text { font-size: 15px; font-weight: 500; letter-spacing: 0.3px; }
  .phone-text { font-size: 50px; font-weight: 500; letter-spacing: 1px; }

  .brand-box {
    position: absolute; left: 876px; top: 15px; width: 224px; height: 152px;
    background: var(--white); display: flex; flex-direction: column;
    justify-content: center; padding-left: 26px;
  }
  .brand-name { font-size: 34px; font-weight: 600; color: var(--brand-blue); line-height: 1.15; letter-spacing: 1px; }

  .practice-list { position: absolute; left: 749px; top: 188px; list-style: none; }
  .practice-list li {
    display: flex; align-items: flex-start; gap: 11px;
    color: var(--white); font-size: 18px; font-weight: 700; line-height: 33px;
  }
  .practice-list svg { flex: none; margin-top: 5px; }
  .practice-list span { max-width: 260px; }

  .web-pill {
    position: absolute; left: 648px; top: 442px; width: 452px; height: 47px;
    border-radius: 24px 0 0 24px;
    background: linear-gradient(90deg, #000 0%, #1c1c1c 55%, #4a4a4a 100%);
    display: flex; align-items: center; padding-left: 92px;
    color: var(--white); font-size: 28px; font-weight: 500; letter-spacing: 0.5px;
  }
</style>
</head>
<body>
  <div class="sign">
    <svg class="sign-art" viewBox="0 0 1100 544" width="1100" height="544">
      <defs>
        <linearGradient id="photoTone" x1="0" y1="0" x2="1" y2="1">
          <stop offset="0" stop-color="var(--photo-blue-a)"/>
          <stop offset="1" stop-color="var(--photo-blue-b)"/>
        </linearGradient>
      </defs>
      <path d="M745 0 Q640 272 722 544 L1100 544 L1100 0 Z" fill="var(--white)"/>
      <path d="M758 0 Q656 272 736 544 L1100 544 L1100 0 Z" fill="var(--deep-blue)"/>
      <g role="img" aria-label="Blue-toned photo of a lawyer in a suit with arms crossed">
        <path d="M774 0 Q674 272 752 544 L1100 544 L1100 0 Z" fill="url(#photoTone)"/>
      </g>
    </svg>

    <div class="headline headline-top">Get your</div>
    <div class="headline headline-bottom">skates on!</div>

    <div class="contact-band email-band">
      <span class="icon-disc">
        <svg width="34" height="26" viewBox="0 0 34 26"><rect x="2" y="2" width="30" height="22" rx="3" fill="none" stroke="#1f2029" stroke-width="3"/><path d="M3 4 L17 15 L31 4" fill="none" stroke="#1f2029" stroke-width="3"/></svg>
      </span>
      <span class="email-text">admin@pelbarnlegal.com</span>
    </div>

    <div class="contact-band phone-band">
      <span class="icon-disc">
        <svg width="30" height="30" viewBox="0 0 24 24"><path fill="#4274c5" d="M6.6 10.8a15.1 15.1 0 0 0 6.6 6.6l2.2-2.2c.3-.3.7-.4 1-.2 1.1.4 2.3.6 3.6.6.6 0 1 .4 1 1V20c0 .6-.4 1-1 1A17 17 0 0 1 3 4c0-.6.4-1 1-1h3.5c.6 0 1 .4 1 1 0 1.3.2 2.5.6 3.6.1.3 0 .7-.2 1L6.6 10.8z"/></svg>
      </span>
      <span class="phone-text">0491 607 238</span>
    </div>

    <div class="brand-box">
      <div class="brand-name">PELBARN</div>
      <div class="brand-name">LEGAL</div>
    </div>

    <ul class="practice-list">
      <li><svg width="22" height="22" viewBox="0 0 22 22"><circle cx="11" cy="11" r="9.5" fill="none" stroke="#cadeef" stroke-width="1.3"/><path d="M7 11.3 L10 14 L15 8" fill="none" stroke="#cadeef" stroke-width="1.3"/></svg><span>Family Law</span></li>
      <li><svg width="22" height="22" viewBox="0 0 22 22"><circle cx="11" cy="11" r="9.5" fill="none" stroke="#cadeef" stroke-width="1.3"/><path d="M7 11.3 L10 14 L15 8" fill="none" stroke="#cadeef" stroke-width="1.3"/></svg><span>Wills and Estates</span></li>
      <li><svg width="22" height="22" viewBox="0 0 22 22"><circle cx="11" cy="11" r="9.5" fill="none" stroke="#cadeef" stroke-width="1.3"/><path d="M7 11.3 L10 14 L15 8" fill="none" stroke="#cadeef" stroke-width="1.3"/></svg><span>Building and Construction</span></li>
      <li><svg width="22" height="22" viewBox="0 0 22 22"><circle cx="11" cy="11" r="9.5" fill="none" stroke="#cadeef" stroke-width="1.3"/><path d="M7 11.3 L10 14 L15 8" fill="none" stroke="#cadeef" stroke-width="1.3"/></svg><span>Corporate and Commercial</span></li>
      <li><svg width="22" height="22" viewBox="0 0 22 22"><circle cx="11" cy="11" r="9.5" fill="none" stroke="#cadeef" stroke-width="1.3"/><path d="M7 11.3 L10 14 L15 8" fill="none" stroke="#cadeef" stroke-width="1.3"/></svg><span>Local Government</span></li>
      <li><svg width="22" height="22" viewBox="0 0 22 22"><circle cx="11" cy="11" r="9.5" fill="none" stroke="#cadeef" stroke-width="1.3"/><path d="M7 11.3 L10 14 L15 8" fill="none" stroke="#cadeef" stroke-width="1.3"/></svg><span>General legal (personal or business)</span></li>
    </ul>

    <div class="web-pill">www.pelbarnlegal.com</div>
  </div>
</body>
</html>
```